Disability provider requiring digital flyer to promote services

My company works within the Disability sector (KVRA registered provider), currently operating in Sydney, Australia.
I require a digital brochure which lists our services and gives potential customers a quick look into what we do with a single glance.
Undecided whether this digital flyer is to be single or double sided, happy to consult with an experienced designer in this regard.
I prefer minimalist designs (which may be an issue for someone trying to convey information, I'm not sure), and possibly someone who can work with out watercolor logo.
Services include:
-Supported Independent Living
-Specialist Disability Accommodation
-Individualised Living Options Stage 1 & 2
-Home Modifications
-Occupational Therapy
-Support Coordination Levels 1 & 2
-Short Term Accommodation - STA Respite
-Drop In Supports
-Community Access

```html
<!DOCTYPE html>
<html lang="en">
<head>
<meta charset="utf-8">
<title>Clearwater Care – Services Flyer</title>
<link href="https://fonts.googleapis.com/css2?family=Montserrat:wght@400;500;800&display=swap" rel="stylesheet">
<style>
:root{
  --page:#f4f4f4;
  --stage:#e6e6e6;
  --teal:#4bbfa8;
  --orange:#f6a45f;
  --ink:#3c3c3c;
  --magenta:#b7358f;
  --card:#fbfbfb;
  --white:#ffffff;
  --i-teal:#3fb89c;--i-red:#e0335f;--i-pink:#e075b5;--i-purple:#8e5fae;
  --i-cyan:#5fc4cc;--i-orange:#f59a4c;--i-yellow:#f8c64a;--i-coral:#f2845a;--i-plum:#a8328f;
}
*{box-sizing:border-box;margin:0;padding:0}
html,body{width:1200px;height:1200px;overflow:hidden}
body{background:var(--stage);font-family:'Montserrat',sans-serif;color:var(--ink)}
.flyer{position:absolute;left:172px;top:0;width:856px;height:1200px;background:var(--page);overflow:hidden}
.brand{position:absolute;left:97px;top:27px;width:206px;text-align:center}
.brand__art{height:130px;border-radius:8px;background:linear-gradient(135deg,#f3a7d2,#f6c48f 60%,#bfe3c8)}
.brand__name{margin-top:14px;font-size:30px;font-weight:500;line-height:1.05;letter-spacing:1px;color:var(--ink)}
.hero{position:absolute;left:439px;top:24px;width:391px;height:428px;border-radius:0 78px 0 78px;
  background:linear-gradient(160deg,#b9dc7a,#7fbf4e 45%,#dfe6ea 70%,#9bbd6a)}
.band{position:absolute;left:0;top:465px;width:856px;height:177px;background:var(--orange)}
.about{position:absolute;left:26px;top:265px;width:391px;height:365px;background:var(--teal);
  border-radius:70px 0 112px 0;padding:40px 29px 0 30px;color:var(--white)}
.about h2{font-size:47px;font-weight:800;line-height:1;margin-bottom:18px;letter-spacing:.3px}
.about p{font-size:19.6px;line-height:25.1px;text-align:justify}
.provide{position:absolute;right:26px;top:470px;text-align:right}
.provide h2{font-size:49px;font-weight:800;line-height:48px;color:var(--ink)}
.provide p{margin-top:16px;font-size:19px;line-height:25px;font-weight:500}
.services{position:absolute;left:26px;top:665px;width:804px;display:grid;list-style:none;
  grid-template-columns:repeat(3,238px);grid-auto-rows:138px;column-gap:45px;row-gap:22px}
.service{background:var(--card);border-radius:28px;box-shadow:0 3px 10px rgba(0,0,0,.06);padding:9px 8px 0 25px;overflow:hidden}
.service__icon{display:block;width:56px;height:56px;margin-left:-3px}
.service__name{margin-top:8px;font-size:16.5px;line-height:20.5px;font-weight:500;white-space:nowrap}
.footer{position:absolute;left:0;bottom:0;width:856px;height:54px;background:var(--magenta);color:var(--white);
  display:flex;align-items:center;padding:0 24px;font-size:14px;gap:15px}
.footer__item{display:flex;align-items:center;gap:3px}
.footer__item svg{width:14px;height:14px}
.footer__rule{width:1px;height:18px;background:var(--white);margin-left:14px}
.footer__social{display:flex;gap:9px;margin-left:14px}
.footer__social span{width:16px;height:16px;border:1.5px solid var(--white);border-radius:50%}
</style>
</head>
<body>
<div class="flyer">
  <div class="brand">
    <div class="brand__art" role="img" aria-label="Watercolour tree with a swing and a person in a wheelchair giving a high five"></div>
    <div class="brand__name">CLEARWATER<br>CARE</div>
  </div>

  <div class="hero" role="img" aria-label="Smiling carer hugging an older woman seated in a wheelchair in a sunny park"></div>

  <div class="band"></div>

  <section class="about">
    <h2>Who We Are</h2>
    <p>Clearwater Care is a Sydney based disability support services provider. Focusing on intellectual, physical &amp; sensory disabilities including mental health within the Greater Sydney region, we strive to assist our participants in leading an independent and fulfilling life.</p>
  </section>

  <header class="provide">
    <h2>What We<br>Provide</h2>
    <p>A Quick look at<br>Clearwater Care’s services:</p>
  </header>

  <ul class="services">
    <li class="service">
      <svg class="service__icon" viewBox="0 0 56 56"><circle cx="28" cy="28" r="28" fill="var(--i-teal)"/><g fill="#fff"><circle cx="21" cy="15" r="4"/><circle cx="35" cy="15" r="4"/><rect x="17" y="21" width="8" height="20" rx="3"/><rect x="31" y="21" width="8" height="20" rx="3"/></g></svg>
      <div class="service__name">Supported<br>Independent Living</div>
    </li>
    <li class="service">
      <svg class="service__icon" viewBox="0 0 56 56"><circle cx="28" cy="28" r="28" fill="var(--i-red)"/><path d="M12 29 28 14l16 15v14H12z" fill="#fff"/><circle cx="28" cy="26" r="2.5" fill="var(--i-red)"/><path d="M26 29v6h6l2 4M24 31a6 6 0 1 0 6 8" fill="none" stroke="var(--i-red)" stroke-width="2"/></svg>
      <div class="service__name">Specialist Disability<br>Accommodation</div>
    </li>
    <li class="service">
      <svg class="service__icon" viewBox="0 0 56 56"><circle cx="28" cy="28" r="28" fill="var(--i-pink)"/><g fill="#fff"><circle cx="24" cy="18" r="6"/><path d="M13 40a11 11 0 0 1 22 0z"/><path d="M33 32l7-4 7 4-7 4z"/><path d="M33 37l7 4 7-4" fill="none" stroke="#fff" stroke-width="2"/></g></svg>
      <div class="service__name">Individualised Living<br>Options Stage 1 &amp; 2</div>
    </li>
    <li class="service">
      <svg class="service__icon" viewBox="0 0 56 56"><circle cx="28" cy="28" r="28" fill="var(--i-purple)"/><g fill="none" stroke="#fff" stroke-width="2"><path d="M12 28 28 13l16 15M16 25v17h24V25"/><path d="M22 38l12-12M22 26l12 12"/></g></svg>
      <div class="service__name">Home Modifications</div>
    </li>
    <li class="service">
      <svg class="service__icon" viewBox="0 0 56 56"><circle cx="28" cy="28" r="28" fill="var(--i-cyan)"/><g fill="#fff"><circle cx="28" cy="15" r="4"/><rect x="13" y="21" width="30" height="4" rx="2"/><path d="M25 24h6l4 20h-4l-3-10-3 10h-4z"/></g></svg>
      <div class="service__name">Occupational Therapy</div>
    </li>
    <li class="service">
      <svg class="service__icon" viewBox="0 0 56 56"><circle cx="28" cy="28" r="28" fill="var(--i-orange)"/><g fill="none" stroke="#fff" stroke-width="2"><circle cx="28" cy="22" r="9"/><path d="M28 31v6M20 28l-5 6M36 28l5 6"/><circle cx="28" cy="40" r="3"/><circle cx="14" cy="37" r="3"/><circle cx="42" cy="37" r="3"/></g></svg>
      <div class="service__name">Support Coordination<br>Levels 1 &amp; 2</div>
    </li>
    <li class="service">
      <svg class="service__icon" viewBox="0 0 56 56"><circle cx="28" cy="28" r="28" fill="var(--i-yellow)"/><g fill="none" stroke="#fff" stroke-width="2"><path d="M11 28 28 13l17 15M16 25v17h24V25"/><circle cx="28" cy="32" r="5"/><path d="M28 29v3h2"/></g></svg>
      <div class="service__name">Short Term<br>Accommodation - STA<br>Respite</div>
    </li>
    <li class="service">
      <svg class="service__icon" viewBox="0 0 56 56"><circle cx="28" cy="28" r="28" fill="var(--i-coral)"/><g fill="#fff"><path d="M28 11c5 7 7 10 7 14a7 7 0 0 1-14 0c0-4 2-7 7-14z"/><path d="M12 30c5 0 8 6 14 12h-5c-5-4-8-8-9-12zM44 30c-5 0-8 6-14 12h5c5-4 8-8 9-12z"/></g></svg>
      <div class="service__name">Drop In Supports</div>
    </li>
    <li class="service">
      <svg class="service__icon" viewBox="0 0 56 56"><circle cx="28" cy="28" r="28" fill="var(--i-plum)"/><g fill="#fff"><circle cx="19" cy="20" r="4"/><circle cx="28" cy="17" r="4.5"/><circle cx="37" cy="20" r="4"/><path d="M11 36a8 8 0 0 1 16 0zM19 33a9 9 0 0 1 18 0zM29 36a8 8 0 0 1 16 0z"/><circle cx="40" cy="38" r="5"/></g></svg>
      <div class="service__name">Community Access</div>
    </li>
  </ul>

  <footer class="footer">
    <span class="footer__item"><svg viewBox="0 0 14 14"><circle cx="7" cy="7" r="6.2" fill="none" stroke="#fff"/><path d="M4.5 4c0 3 2.5 5.5 5.5 5.5l.5-1.5-1.5-.8-.8.8c-1-.4-1.8-1.2-2.2-2.2l.8-.8L6 3.5z" fill="#fff"/></svg>+61 0400 123 456</span>
    <span class="footer__item"><svg viewBox="0 0 14 14"><circle cx="7" cy="7" r="6.2" fill="none" stroke="#fff"/><rect x="3.8" y="4.8" width="6.4" height="4.4" fill="none" stroke="#fff" stroke-width=".9"/><path d="M3.8 4.8 7 7.3l3.2-2.5" fill="none" stroke="#fff" stroke-width=".9"/></svg>hello@clearwatercare.com.au</span>
    <span class="footer__item"><svg viewBox="0 0 14 14"><circle cx="7" cy="7" r="6.2" fill="none" stroke="#fff"/><circle cx="7" cy="7" r="3.5" fill="none" stroke="#fff" stroke-width=".9"/><path d="M3.5 7h7M7 3.5v7" stroke="#fff" stroke-width=".9"/></svg>www.clearwatercare.com.au</span>
    <span class="footer__rule"></span>
    <span class="footer__social"><span></span><span></span><span></span></span>
  </footer>
</div>
</body>
</html>
```